Brisk Marlow website (tool sales website)

place to sell tools that are used to install tiles. We have over 100 tools that can be divided into 5-6 categories we plan to sell our tools online

The business purchases tools wholesale and sells them to customers retail via social media and soon by online website

The product consists of tools and the blades that are used mostly to cut and install tiles like floor tile, shower tiles

Target Market(s)

The target market includes individuals in the building trade and those learning the trade. For example trade schools have used this business exclusively for the tools they need.

Industry/Entity Type

Sales

Coding

Coded - Design and coding required

Number of Pages Required

1 page

Requirements
Must have
• Color and imagery complimentary to the attached logo
• We have approximately 100 items for sale now and think a home page and 5 pages with different tool categories might work best. Categories would be Dimond blade cutting; Coring and Drilling; Grinding and polishing; Manual tile cutters; Other.
• Really only need the space on each page to put the items. We can use Dreamweaver to place actual items and finish the site.
Nice to have
• Need to incorporate a cart for purchases
• We envision something like the US retailer Halvorne's website, just not as complex. Home page with general info and 5 areas to go to 5 pages each with multiple spots for tools to be listed with info. There is a screen shot below as an example of one of the five
• pages

```html
<!DOCTYPE html>
<html lang="en">
<head>
<meta charset="utf-8">
<title>Brisk Marlow's Diamond Blades</title>
<link rel="stylesheet" href="https://fonts.googleapis.com/css2?family=Nunito:wght@400;600;700;800&family=Open+Sans:wght@400;600&display=swap">
<style>
:root{
  --red:#a3000f;
  --red-dark:#7d000b;
  --ink:#222;
  --muted:#666;
  --topbar:#e6e6e6;
  --line:#d6d6d6;
  --footer:#232323;
  --white:#fff;
  --placeholder-light:#f2f2f2;
  --placeholder-dark:#d4d4d4;
}
*{box-sizing:border-box;margin:0;padding:0}
html,body{width:1200px;height:2922px;overflow:hidden;background:var(--white)}
body{position:relative;font-family:"Open Sans",sans-serif;color:var(--ink)}
.abs{position:absolute}
a{color:inherit;text-decoration:none}

.topbar{left:0;top:0;width:1200px;height:51px;background:var(--topbar)}
.toplinks{right:248px;top:0;height:51px;display:flex;align-items:center;gap:10px;font-size:14px;color:#555;white-space:nowrap}
.toplinks span.sep{color:#888}
.login{left:968px;top:0;width:117px;height:51px;background:var(--red);color:var(--white);display:flex;align-items:center;justify-content:center;gap:8px;font-size:17px;font-family:"Nunito",sans-serif;font-weight:600}

.logo-disc{left:120px;top:100px;width:200px;height:166px;background:var(--white);border-radius:0 0 100px 100px;z-index:2}
.brand-dot{left:160px;top:70px;width:120px;height:120px;border-radius:50%;background:var(--red);z-index:3}
.brand{left:322px;top:114px;width:360px;font-family:"Nunito",sans-serif;font-weight:800;font-size:32px;line-height:34px;color:#1a1a1a}
.bag{left:968px;top:74px;display:flex;gap:10px;align-items:center;font-size:13px;color:#666;line-height:16px}
.bag b{font-weight:400;font-size:16px}
.search{left:697px;top:136px;width:388px;height:43px;border:2px solid var(--line);display:flex;align-items:center;padding-left:14px;gap:12px;font-size:13px;color:#888}

.nav{left:0;top:214px;width:1200px;height:59px;background:var(--red);z-index:1}
.nav ul{position:absolute;left:306px;top:0;display:flex;list-style:none;height:59px}
.nav li{height:59px;display:flex;align-items:center;justify-content:center;color:var(--white);font-family:"Nunito",sans-serif;font-size:18px;border-right:1px solid rgba(255,255,255,.35)}
.nav li.active{background:var(--red-dark)}
.nav li:last-child{border-right:0}

.hero{left:0;top:273px;width:1200px;height:565px}
.hero-text{left:130px;top:448px;color:var(--white);font-family:"Nunito",sans-serif}
.hero-text .l1{font-size:36px;font-weight:400;letter-spacing:1px}
.hero-text .l2{font-size:42px;font-weight:700;letter-spacing:1px;margin-top:2px}
.shop{left:132px;top:563px;width:215px;height:51px;border:2px solid var(--white);color:var(--white);display:flex;align-items:center;justify-content:center;font-family:"Nunito",sans-serif;font-size:21px}
.dots{left:557px;top:789px;display:flex;gap:8px}
.dots i{width:15px;height:15px;border-radius:50%;background:var(--white)}
.dots i:first-child{background:transparent;border:2px solid var(--white)}

.heading{left:0;width:1200px;text-align:center;font-family:"Nunito",sans-serif;font-weight:400;font-size:31px;letter-spacing:.5px;color:#222}
.heading::after{content:"";display:block;width:150px;height:2px;background:#777;margin:8px auto 0}
.heading.short::after{width:205px}
.sub{left:0;width:1200px;top:951px;text-align:center;font-size:16px;color:#555}
.para{left:190px;width:826px;top:994px;text-align:center;font-size:14px;line-height:25px;color:#666}
.learn{left:520px;top:1095px;width:166px;height:43px;border:2px solid var(--red);color:var(--red);display:flex;align-items:center;justify-content:center;font-family:"Nunito",sans-serif;font-weight:700;font-size:16px}

.tile{display:flex;align-items:center;justify-content:center;text-align:center;color:var(--white);font-family:"Nunito",sans-serif;font-size:24px;line-height:28px;letter-spacing:.5px}
.tile span::after{content:"";display:block;width:80px;height:3px;background:var(--white);margin:8px auto 0}
.tile.small{font-size:22px;line-height:26px}

.rule{left:121px;top:1701px;width:966px;height:1px;background:var(--line)}

.product{border:1px solid #ccc;background:var(--white);text-align:center;font-family:"Nunito",sans-serif}
.product .img{position:absolute;left:30px;top:38px;width:172px;height:156px;background:linear-gradient(180deg,var(--placeholder-light),var(--placeholder-dark))}
.product .title{position:absolute;left:0;right:0;top:222px;font-size:19px}
.product .price{position:absolute;left:0;right:0;top:250px;font-size:17px;color:#333}
.buy{position:absolute;left:58px;top:280px;width:117px;height:31px;background:var(--red);color:var(--white);font-size:14px;font-weight:700;display:flex;align-items:center;justify-content:center}

.promo{border:1px solid #ccc;background:var(--white);text-align:center}
.promo .img{position:absolute;left:0;top:0;width:100%;height:216px}
.promo h3{position:absolute;left:0;right:0;top:242px;font-family:"Nunito",sans-serif;font-weight:400;font-size:23px;color:#222}
.promo p{position:absolute;left:22px;right:22px;top:277px;font-size:13px;line-height:21px;color:#777}
.promo .click{position:absolute;left:91px;top:364px;width:129px;height:34px;background:var(--red);color:var(--white);font-family:"Nunito",sans-serif;font-weight:700;font-size:14px;display:flex;align-items:center;justify-content:center}

.footer{left:0;top:2680px;width:1200px;height:242px;background:var(--footer)}
.f-brand{left:130px;top:2800px;width:180px;text-align:center;font-family:"Nunito",sans-serif;font-weight:800;font-size:17px;line-height:19px;color:var(--white)}
.f-dot{left:190px;top:2700px;width:60px;height:60px;border-radius:50%;background:var(--red)}
.cards{left:130px;top:2856px;display:flex;gap:8px}
.cards i{width:38px;height:22px;background:#ddd;border-radius:3px}
.social{left:422px;top:2719px;display:flex;gap:13px}
.social i{width:56px;height:56px;border-radius:50%;background:#4a6aa8}
.social i:nth-child(2){background:#4fb3e8}
.social i:nth-child(3){background:#d6453b}
.social i:nth-child(4){background:#3c6d9c}
.social i:nth-child(5){background:#3f6c99}
.social i.mail{background:#3cb7d4;display:flex;align-items:center;justify-content:center}
.flinks{left:366px;top:2812px;display:flex;gap:26px;font-size:11px;color:#ddd;font-family:"Nunito",sans-serif}
.copy{left:330px;width:520px;top:2856px;text-align:center;font-size:11px;color:#ccc}
</style>
</head>
<body>

<div class="abs topbar"></div>
<nav class="abs toplinks"><a>My Account</a><span class="sep">|</span><a>Wishlist</a><span class="sep">|</span><a>Create account</a><span class="sep">|</span><a>Support</a></nav>
<a class="abs login"><svg width="14" height="17" viewBox="0 0 14 17"><rect x="1" y="7" width="12" height="10" rx="1" fill="#fff"/><path d="M3.5 7V5a3.5 3.5 0 0 1 7 0v2" stroke="#fff" stroke-width="2" fill="none"/></svg>Log In</a>

<div class="abs logo-disc"></div>
<div class="abs brand-dot"></div>
<div class="abs brand">Brisk Marlow's<br>Diamond Blades</div>

<div class="abs bag">
  <svg width="44" height="42" viewBox="0 0 44 42"><path d="M13 14V10a9 9 0 0 1 18 0v4" stroke="#3aa935" stroke-width="3" fill="none"/><rect x="4" y="14" width="36" height="26" rx="2" fill="#3aa935"/></svg>
  <div>My Bag<br><b>0 items</b></div>
</div>
<div class="abs search"><svg width="18" height="18" viewBox="0 0 18 18"><circle cx="7.5" cy="7.5" r="5.5" stroke="#888" stroke-width="2" fill="none"/><path d="M12 12l5 5" stroke="#888" stroke-width="2"/></svg>Enter Keyword here</div>

<nav class="abs nav">
  <ul>
    <li class="active" style="width:117px">HOME</li>
    <li style="width:148px">ABOUT US</li>
    <li style="width:200px">OUR PRODUCTS</li>
    <li style="width:166px">CATEGORIES</li>
    <li style="width:166px">CONTACT US</li>
  </ul>
</nav>

<svg class="abs hero" viewBox="0 0 1200 565" role="img" aria-label="Black and white photo of stacked diamond saw blades">
  <defs><linearGradient id="heroGrad" x1="0" y1="0" x2="1" y2="1"><stop offset="0" stop-color="#8a8a8a"/><stop offset=".45" stop-color="#4a4a4a"/><stop offset="1" stop-color="#777"/></linearGradient></defs>
  <path d="M0 0H1200V495L600 565L0 495Z" fill="url(#heroGrad)"/>
</svg>
<div class="abs hero-text"><div class="l1">WE SELL QUALITY</div><div class="l2">TOOLS AND BLADES</div></div>
<a class="abs shop">SHOP NOW</a>
<div class="abs dots"><i></i><i></i><i></i><i></i></div>

<h2 class="abs heading" style="top:880px">ABOUT COMPANY</h2>
<p class="abs sub">Praesent elementum elit at tellus nec ultricies sit amet porttitor mattis enim</p>
<p class="abs para">Mauris vel lacus vitae felis vestibulum volutpat Etiam est nunc venenatis in tristique eu imperdiet ac nisl Cum sociis natoque penatibus et magnis dis parturient montes nascetur ridiculus mus In iaculis facilisis massa Etiam eu urna Sed porta Suspendisse quam leo molestie sed luctus quis feugiat in pede Fusce tellus Sed metus</p>
<a class="abs learn">LEARN MORE</a>

<div class="abs tile" role="img" aria-label="Photo of a saw cutting with a diamond blade" style="left:121px;top:1208px;width:477px;height:230px;background:linear-gradient(135deg,#4a4a4a,#222 60%,#5a5a5a)"><span>DIAMOND BLADE CUTTING</span></div>
<div class="abs tile" role="img" aria-label="Red-toned photo of a coring drill" style="left:610px;top:1208px;width:477px;height:230px;background:linear-gradient(135deg,#b3101f,#7a0612 60%,#a10c1b)"><span>CORING AND DRILLING</span></div>
<div class="abs tile small" role="img" aria-label="Photo of a grinding and polishing pad" style="left:121px;top:1447px;width:311px;height:228px;background:linear-gradient(135deg,#5a4e42,#2c2620 60%,#6b5c4a)"><span>GRINDING AND<br>POLISHING</span></div>
<div class="abs tile small" role="img" aria-label="Photo of a manual tile cutter on tiles" style="left:448px;top:1447px;width:312px;height:228px;background:linear-gradient(135deg,#8c8c8c,#555 60%,#7a7a7a)"><span>MANUAL TILE<br>CUTTERS</span></div>
<div class="abs tile small" role="img" aria-label="Photo of a circular saw blade on wood" style="left:775px;top:1447px;width:312px;height:228px;background:linear-gradient(135deg,#5a4a3a,#2a2018 60%,#4a3a2a)"><span>OTHER</span></div>

<div class="abs rule"></div>

<h2 class="abs heading short" style="top:1738px;font-size:28px">LATEST PRODUCTS</h2>

<div class="abs product" style="left:119px;top:1812px;width:234px;height:343px"><div class="img" role="img" aria-label="Product photo of a diamond saw blade"></div><div class="title">Product Tittle</div><div class="price">$150.00</div><a class="buy">BUY NOW</a></div>
<div class="abs product" style="left:364px;top:1812px;width:234px;height:343px"><div class="img" role="img" aria-label="Product photo of a manual tile cutter"></div><div class="title">Product Tittle</div><div class="price">$150.00</div><a class="buy">BUY NOW</a></div>
<div class="abs product" style="left:610px;top:1812px;width:233px;height:343px"><div class="img" role="img" aria-label="Product photo of a wire brush wheel"></div><div class="title">Product Tittle</div><div class="price">$150.00</div><a class="buy">BUY NOW</a></div>
<div class="abs product" style="left:855px;top:1812px;width:236px;height:343px"><div class="img" role="img" aria-label="Product photo of a core drill bit"></div><div class="title">Product Tittle</div><div class="price">$150.00</div><a class="buy">BUY NOW</a></div>

<div class="abs promo" style="left:123px;top:2242px;width:311px;height:384px"><div class="img" role="img" aria-label="Photo of an angle grinder throwing sparks" style="background:linear-gradient(135deg,#c07020,#3a2414 70%)"></div><h3>WHY CHOOSE US</h3><p>ullamcorper est eget tempor cursus neque mi consectetuer mi a ultricies massa est sed nisl Class aptent taciti</p><a class="click">CLICK HERE</a></div>
<div class="abs promo" style="left:448px;top:2242px;width:312px;height:384px"><div class="img" role="img" aria-label="Photo of a floor sander on wooden boards" style="background:linear-gradient(180deg,#9a9a9a,#6a5a48 55%,#b08050)"></div><h3>BEST SELLERS</h3><p>ullamcorper est eget tempor cursus neque mi consectetuer mi a ultricies massa est sed nisl Class aptent taciti socio</p><a class="click">CLICK HERE</a></div>
<div class="abs promo" style="left:775px;top:2242px;width:312px;height:384px"><div class="img" role="img" aria-label="Photo of hands holding a blade to a grinding wheel" style="background:linear-gradient(135deg,#7a8a9a,#3a4048 50%,#c0a080)"></div><h3>TOP DEALS</h3><p>ullamcorper est eget tempor cursus neque mi consectetuer mi a ultricies massa est sed nisl Class aptent taciti</p><a class="click">CLICK HERE</a></div>

<footer class="abs footer"></footer>
<div class="abs f-dot"></div>
<div class="abs f-brand">Brisk Marlow's<br>Diamond Blades</div>
<div class="abs cards"><i></i><i></i><i></i><i></i></div>
<div class="abs social"><i></i><i></i><i></i><i></i><i></i><i class="mail"><svg width="24" height="18" viewBox="0 0 24 18"><rect x="1" y="1" width="22" height="16" rx="1" fill="none" stroke="#fff" stroke-width="2"/><path d="M1 2l11 8 11-8" fill="none" stroke="#fff" stroke-width="2"/></svg></i></div>
<nav class="abs flinks"><a>HOME</a><span>|</span><a>ABOUT US</a><span>|</span><a>SERVICES</a><span>|</span><a>PRODUCTS</a><span>|</span><a>CONTACT US</a></nav>
<p class="abs copy">© Copyrights 2017 Brisk Marlow All Rights Reserved.</p>

</body>
</html>
```